Health & Fitness Author & Public Speaker Needs Visually Stunning Web Redesign!

It's time for a redesign of the home page for Verity Halloway's "Bright Fork Kitchen" website (www.brightforkkitchen-example.com). We have a VERY clear idea of what we want, so it really won't take a talented designer long to bring it to life.
The website itself is used to promote & sell her range of health & nutrition programs to a female audience, primarily aged 24 - 35 working in professional or semi professional occupations.
For a VERY comprehensive outline of exactly what we are after, please see the following attached files:
(1) 'Website - WireFrame' (layout, content/copy, visual design style we want along with the desired color scheme)
(2) 'Website - Style Guide' (these are the colours, and overall feel we want)
PLEASE REVIEW THIS IN FULL - THEY WILL GIVE YOU A VERY CLEAR IDEA OF WHAT WE WANT.
Most of the files you need are attached, but for more photos that you can use (of Verity, her programs, and food/meals) can be found at these URL's:
VERITY (profile photos):
https://www.filebinbox.example/sh/qm3rt8wpz1xkd7a/RtPlm4vaNe
ECOVERS
- Bright Fork Kitchen Guide (ebook): https://www.filebinbox.example/sh/wxtnvo5d274ku22/hBqYrsnoz3
- 21 Week Total Momentum Course (ecourse): https://www.filebinbox.example/sh/zopqinr6a2mhwyl/c-dg341oTR
- E-Magazine Issues:
https://www.filebinbox.example/sh/4pzmkar2s9vtyw/57LeWcdDxpB
STOCK IMAGES:
https://www.filebinbox.example/sh/k2qowr8atbnzlx/Qe3HT5mmDy
As we will need to revamp our existing Circlepage page & other printed material, there may be the potential for further work for the successful designer in the future.
Thanks & Good Luck!
Declan Furrow
Marketing & Business Development Manager
Bright Fork Kitchen

```html
<!DOCTYPE html>
<html lang="en">
<head>
<meta charset="utf-8">
<title>Bright Fork Kitchen — Home</title>
<link rel="stylesheet" href="https://fonts.googleapis.com/css2?family=Varela+Round&family=Open+Sans:wght@400;600;700&family=Hind:wght@500;600&family=Oswald:wght@500;600&display=swap">
<style>
:root{
  --magenta:#e8185a;
  --purple:#93109a;
  --purple-dark:#7d0b86;
  --ink:#333;
  --muted:#555;
  --page:#efeff0;
  --white:#fff;
  --panel:rgba(35,35,35,.88);
  --fb-blue:#3b5998;
  --rule:#cfcfcf;
}
*{box-sizing:border-box;margin:0;padding:0}
html,body{width:861px;height:1200px;overflow:hidden}
body{position:relative;background:var(--page);font-family:"Open Sans",sans-serif;color:var(--ink)}
.abs{position:absolute}

/* top bar & header */
.topbar{left:0;top:0;width:861px;height:19px;background:var(--purple);color:var(--white);font-size:10px;display:flex;justify-content:flex-end;align-items:center;gap:14px;padding-right:90px}
.topbar span{display:flex;align-items:center;gap:4px}
.header{left:72px;top:0;width:715px;height:71px;background:var(--white);border-radius:0 0 10px 10px;box-shadow:0 2px 6px rgba(0,0,0,.2);z-index:3}
.header::before{content:"";position:absolute;left:140px;right:0;top:0;height:19px;background:var(--purple)}
.brand{left:16px;top:20px;font-family:"Varela Round",sans-serif;font-size:17px;color:var(--magenta);display:flex;align-items:center;gap:6px}
.brand i{width:12px;height:12px;border-radius:50%;background:var(--purple);display:block}
.nav{left:266px;top:34px;display:flex;font-family:"Hind",sans-serif;font-weight:600;font-size:11.5px;letter-spacing:.5px;color:#444}
.nav a{color:inherit;text-decoration:none;padding:0 20px;height:34px;line-height:24px;border-left:1px solid #ddd}
.nav a:first-child{border:0;padding:0}
.nav a.active{background:var(--magenta);color:var(--white);padding:0 8px;height:24px;margin-right:20px}

/* hero */
.hero{left:0;top:0;width:861px;height:469px;background:radial-gradient(ellipse at 62% 40%,#d8a98f 0%,#c49a88 22%,#b5aaa2 45%,#a7a29c 75%,#8f8a86 100%)}
.hero-rule{left:0;top:469px;width:861px;height:5px;background:var(--magenta)}
.signup{left:72px;top:164px;width:228px;height:222px;background:var(--panel);border-radius:6px;padding:16px 17px}
.signup h2{font-family:"Hind",sans-serif;font-weight:600;font-size:18px;line-height:24px;color:var(--white);letter-spacing:.5px}
.signup h2 em{font-style:normal;color:var(--magenta)}
.field{display:block;width:183px;height:24px;border-radius:12px;background:var(--white);border:2px solid #ccc;font-size:9.5px;color:#999;padding:4px 8px;margin-top:12px}
.signup .field:first-of-type{margin-top:14px}
.hook{position:absolute;right:24px;bottom:30px;background:var(--magenta);color:var(--white);font-family:"Hind",sans-serif;font-weight:600;font-size:12px;border:2px solid var(--white);border-radius:8px;padding:4px 11px;box-shadow:0 1px 3px rgba(0,0,0,.4)}
.tagline{left:408px;top:327px;width:453px;height:59px;background:rgba(120,120,120,.45);border-radius:10px 0 0 10px;padding:6px 0 0 17px;font-family:"Hind",sans-serif;font-weight:600}
.tagline strong{display:block;font-size:23px;line-height:26px;color:var(--white);text-shadow:1px 1px 2px rgba(0,0,0,.5)}
.tagline span{display:block;font-size:15px;color:var(--magenta);padding-left:70px;text-shadow:0 0 2px rgba(0,0,0,.3)}

/* posts */
.post{left:60px;width:459px}
.post h1{font-family:"Varela Round",sans-serif;font-weight:400;font-size:20.5px;line-height:26px;color:var(--purple)}
.meta{font-size:8.5px;margin:9px 0 17px 1px;color:#333}
.meta a{color:var(--magenta);text-decoration:none}
.post p{font-size:10px;line-height:14px;text-align:justify;color:var(--ink);margin-bottom:14px}
.share{display:flex;gap:6px;align-items:center;margin-top:8px;font-size:8.5px}
.share b{font-weight:600;height:16px;line-height:16px;padding:0 6px;border-radius:2px;color:var(--white)}
.share .s1{background:#4a6aa5}.share .s2{background:#3fa0d7}.share .s3{background:#e6e6e6;color:#555;border:1px solid #ccc}.share .s4{background:#2a8a3e}
.share .s5{background:#eef0f5;color:#3b5998;border:1px solid #ccc}.share .s6{background:#fff;color:#333;border:1px solid #ccc}.share .s7{background:#f3f3f3;color:#d33;border:1px solid #ccc}
.divider{height:1px;background:var(--rule);margin-top:22px}

/* sidebar */
.ad{left:550px;width:275px}
.guide{top:490px;height:229px;background:linear-gradient(135deg,#f4f1ea 0%,#e9dccc 38%,#c84a3a 70%,#7a9a3a 100%);border:1px solid #ddd}
.guide .copy{position:absolute;left:25px;top:10px;font-family:"Oswald",sans-serif;line-height:1}
.guide .the{font-size:15px;color:#333;margin-left:80px;font-style:normal}
.guide .ult{font-size:38px;color:var(--magenta);font-weight:500}
.guide .lce{font-size:17px;color:var(--purple)}
.guide .g{font-size:40px;color:#222;font-weight:600}
.cta{display:inline-block;background:var(--purple);color:var(--white);font-family:"Oswald",sans-serif;font-weight:500;font-size:14px;padding:6px 8px;border-radius:3px}
.guide .cta{position:absolute;left:26px;top:115px}
.challenge{top:749px;height:164px;background:#ecebf2;border:1px solid #ddd}
.challenge .photo{position:absolute;left:0;top:0;width:134px;height:162px;background:linear-gradient(140deg,#c01ab8,#e46fc0 45%,#a8c070 75%,#6a2a6a)}
.challenge .copy{position:absolute;left:141px;top:10px;font-family:"Oswald",sans-serif;line-height:1}
.challenge .wk{font-size:28px;color:var(--purple);font-weight:600}
.challenge .ch{font-size:23px;color:var(--magenta);font-weight:600}
.challenge .hh{font-size:11.5px;color:#222;margin-top:6px}
.challenge .nt{font-size:17px;color:#222;font-weight:600}
.challenge .cta{position:absolute;left:146px;top:106px;padding:6px 9px}
.fb{top:930px;height:207px;background:var(--white);border:1px solid #c6c6c6}
.fb-head{height:29px;background:var(--fb-blue);color:var(--white);font-family:"Open Sans",sans-serif;font-weight:700;font-size:15px;padding:4px 16px}
.fb-page{display:flex;gap:12px;padding:11px 0 0 16px}
.fb-page .mini{font-family:"Varela Round",sans-serif;color:var(--magenta);font-size:10px;width:76px;line-height:12px;padding-top:6px}
.fb-page .name{font-size:10.5px;color:#3b5998;letter-spacing:.5px;font-weight:600}
.fb-page .likes{font-size:9px;margin-top:6px;display:flex;gap:5px;align-items:center}
.fb-page .likes b{font-weight:400;color:#3b5998;border:1px solid #bbb;background:#eef0f5;padding:1px 4px;font-size:8.5px}
.fb-list{margin:10px 20px 0 18px;border-top:1px solid #e3e3e3}
.fb-item{display:flex;gap:10px;padding-top:6px;margin-bottom:6px}
.fb-item .thumb{width:30px;height:34px;flex:none;border-radius:50%;background:radial-gradient(circle,#9bd04a,#5d9a2a)}
.fb-item .thumb.dark{background:radial-gradient(circle,#6a7a5a,#222)}
.fb-item p{font-size:9px;line-height:11.5px;letter-spacing:.3px;text-align:justify}
.fb-item p b{color:#3b5998;font-weight:600}
.fb-foot{margin:0 20px 0 26px;border-top:1px solid #e3e3e3;font-size:7.5px;color:#555;padding-top:4px;display:flex;gap:5px;align-items:center}
.fb-foot i{width:9px;height:9px;background:var(--fb-blue);display:block}

/* footer */
.footer{left:0;top:1158px;width:861px;height:42px;background:var(--magenta)}
.footer-links{position:absolute;left:54px;top:13px;font-size:9px;font-weight:600;color:var(--white)}
.footer-links span{margin:0 6px}
.social{position:absolute;right:31px;top:6px;display:flex;gap:8px}
.social i{display:block;width:27px;height:27px;background:var(--white);border-radius:2px}
</style>
</head>
<body>

<div class="abs hero" role="img" aria-label="Photo of a woman in an orange sports top resting with her hands on her head on a sunny pebble beach"></div>
<div class="abs hero-rule"></div>

<div class="abs topbar">
  <span>
    <svg width="13" height="9" viewBox="0 0 13 9"><rect x=".5" y=".5" width="12" height="8" fill="none" stroke="#fff"/><path d="M.5 .5l6 4.5 6-4.5" fill="none" stroke="#fff"/></svg>
    hello@brightforkkitchen-example.com
  </span>
  <span>
    <svg width="11" height="11" viewBox="0 0 11 11"><circle cx="5.5" cy="5.5" r="5" fill="none" stroke="#fff"/><path d="M3.5 3c0 3 1.5 4.5 4 5" stroke="#fff" fill="none" stroke-width="1.3"/></svg>
    1800.555.214
  </span>
</div>

<header class="abs header">
  <div class="abs brand"><i></i>Bright Fork Kitchen</div>
  <nav class="abs nav">
    <a class="active">ABOUT VERITY</a>
    <a>THE MAGAZINE</a>
    <a>BLOG &amp; VIDEOS</a>
    <a>SHOP</a>
  </nav>
</header>

<form class="abs signup">
  <h2>Get my <em>FREE monthly</em><br>E-Magazine</h2>
  <span class="field">Your Name</span>
  <span class="field">Your Email</span>
  <span class="hook">HOOK ME UP</span>
</form>

<div class="abs tagline">
  <strong>Get Slim Boost Energy Guilt Free</strong>
  <span>Creating A Healthy Lifestyle You Love</span>
</div>

<article class="abs post" style="top:484px">
  <h1>Integer placerat, tellus et blandit molestie, purus leo semper massa, scelerisque</h1>
  <div class="meta">11th January 2012 // by <a>Miriam Toller</a> // <a>7 comments</a></div>
  <p>Lorem ipsum dolor sit amet, consectetur adipiscing elit. Donec at tortor eget lorem porta aliquam. Praesent eget dolor quam, sit amet porttitor tortor. Curabitur ut nisi felis. Donec sed justo neque. Integer placerat, tellus et blandit molestie, purus leo semper massa, scelerisque dictum purus enim nec est. Aenean in mi tortor. Fusce sed mi urna. Phasellus vitae risus id erat fermentum suscipit. Aliquam mattis, odio vel adipiscing tincidunt, orci augue tincidunt turpis, at dapibus quam elit vitae turpis. Maecenas egestas nibh est. Phasellus suscipit tincidunt ligula, sit amet tristique turpis.</p>
  <div class="share"><b class="s1">Share</b><b class="s2">Post</b><b class="s3">Email</b><b class="s4">Share</b><b class="s5">Like</b><b class="s6">23</b><b class="s7">+1</b></div>
  <div class="divider"></div>
</article>

<article class="abs post" style="top:742px">
  <h1>In hac habitasse platea dictumst. Duis a consequat nisl viverra facilis</h1>
  <div class="meta">11th January 2012 // by <a>Miriam Toller</a> // <a>7 comments</a></div>
  <p>Nullam eleifend risus vitae massa tincidunt eu feugiat diam vestibulum. Cum sociis natoque penatibus et magnis dis parturient montes, nascetur ridiculus mus. Donec fringilla suscipit diam vel tempus. Cum sociis natoque penatibus et magnis dis parturient montes, nascetur ridiculus mus. Phasellus pellentesque scelerisque ante, nec pulvinar eros euismod eget. Nunc in ullamcorper nunc. Nulla euismod, nisl hendrerit convallis blandit, diam turpis lobortis nunc, vitae ultricies turpis lacus vel magna. Class aptent taciti sociosqu ad litora torquent per conubia nostra, per inceptos himenaeos. In hac habitasse platea dictumst. Sed placerat magna non enim blandit ac fermentum mauris elementum. Vivamus malesuada est a justo posuere lobortis. Nullam vel gravida mi. Etiam pellentesque, ligula nec iaculis bibendum, nunc neque euismod nulla, a molestie enim velit a libero.</p>
  <p>Phasellus viverra lorem vel magna eleifend venenatis. Integer convallis sapien at lorem ullamcorper sed viverra massa tempus. Quisque interdum magna vitae ipsum cursus porta. Nam eget pellentesque dolor. Pellentesque habitant morbi tristique senectus et netus et malesuada fames ac turpis egestas. Nullam eleifend risus vitae massa tincidunt eu feugiat diam vestibulum.</p>
  <div class="share"><b class="s1">Share</b><b class="s2">Post</b><b class="s3">Email</b><b class="s4">Share</b><b class="s5">Like</b><b class="s6">23</b><b class="s7">+1</b></div>
  <div class="divider"></div>
</article>

<aside class="abs ad guide" role="img" aria-label="Close-up photo of a fresh salad with tomato, red onion and green pepper">
  <div class="copy">
    <div class="the">the</div>
    <div class="ult">Ultimate</div>
    <div class="lce">Bright Fork Kitchen</div>
    <div class="g">GUIDE</div>
  </div>
  <span class="cta">GET IT NOW!</span>
</aside>

<aside class="abs ad challenge">
  <div class="photo" role="img" aria-label="Photo of a bowl of leafy salad with a fork on a pink background"></div>
  <div class="copy">
    <div class="wk">12 WEEK</div>
    <div class="ch">CHALLENGE</div>
    <div class="hh">HEALTHY, HAPPY &amp; HOT</div>
    <div class="nt">IN NO TIME FLAT!</div>
  </div>
  <span class="cta">JOIN US NOW</span>
</aside>

<aside class="abs ad fb">
  <div class="fb-head">Circlepage</div>
  <div class="fb-page">
    <div class="mini">Bright Fork Kitchen</div>
    <div>
      <div class="name">Bright Fork Kitchen</div>
      <div class="likes"><b>Like</b>3,564 people like this.</div>
    </div>
  </div>
  <div class="fb-list">
    <div class="fb-item"><span class="thumb" role="img" aria-label="Green apple photo"></span><p><b>Eat plain popcorn</b> when you are on a diet. It is a low-calorie snack with high fiber.</p></div>
    <div class="fb-item"><span class="thumb dark" role="img" aria-label="Stacked stones and plant photo"></span><p><b>Eat plain popcorn</b> when you are on a diet. It is a low-calorie snack with high fiber.</p></div>
  </div>
  <div class="fb-foot"><i></i>Circlepage social plugin</div>
</aside>

<footer class="abs footer">
  <div class="footer-links">Community<span>|</span>Free<span>|</span>Resources<span>|</span>Press<span>|</span>Contact</div>
  <div class="social"><i></i><i></i><i></i></div>
</footer>

</body>
</html>
```